Professional letterhead for engineering type firm.

I would like to have a professional looking letterhead for a small HVAC testing company/engineering-type firm. I would like to see designs that show a professional level of expertise and established company. Traditional letterhead designs are a good place to start.
We are a QRTV certified company (which is a big deal in our industry). I have included the QRTV logo, but would like the green in QRTV logo to be black.
Presently, we work out of house so i would not like to include our address at this point.
Information to include:
Phone: 410-555-0162
Website: www.Kestro-VUN.com
Email: Info@Kestro-VUN.com

```html
<!DOCTYPE html>
<html lang="en">
<head>
<meta charset="utf-8">
<title>Kestro VUN Letterhead</title>
<link rel="stylesheet" href="https://fonts.googleapis.com/css2?family=Lato:wght@400;700;900&family=Montserrat:wght@400&display=swap">
<style>
  :root {
    --navy: #29318a;
    --red: #e31d25;
    --ink: #111111;
    --body: #6d6d6d;
    --backdrop: #e2e2e2;
    --paper: #ffffff;
  }
  * { box-sizing: border-box; margin: 0; padding: 0; }
  html, body { width: 1153px; height: 1200px; overflow: hidden; }
  body { background: var(--backdrop); font-family: "Lato", sans-serif; position: relative; }
  .letterhead {
    position: absolute; left: 126px; top: 17px;
    width: 900px; height: 1166px;
    background: var(--paper);
    box-shadow: 0 6px 24px rgba(0,0,0,0.12);
    overflow: hidden;
  }
  .header-swoosh { position: absolute; left: 0; top: 0; width: 900px; height: 220px; }
  .brand {
    position: absolute; left: 90px; top: 72px;
    display: flex; align-items: center; gap: 16px;
  }
  .brand-dot { width: 76px; height: 76px; border-radius: 50%; background: var(--paper); }
  .brand-name {
    font-family: "Lato", sans-serif; font-weight: 900; font-size: 44px;
    color: var(--ink); letter-spacing: 1px; margin-top: 24px;
  }
  .contact {
    position: absolute; left: 618px; top: 86px;
    border-left: 2px solid var(--red); padding-left: 10px;
    font-family: "Montserrat", sans-serif; font-size: 15px; color: var(--ink);
    line-height: 20.5px;
  }
  .contact-row { display: flex; align-items: center; gap: 6px; }
  .contact-row svg { width: 11px; height: 11px; fill: var(--red); }
  .recipient { position: absolute; left: 84px; top: 294px; color: var(--ink); }
  .recipient-name { font-size: 18px; font-weight: 700; }
  .recipient-title { font-size: 13.5px; font-weight: 700; margin-top: 3px; }
  .letter-date { position: absolute; right: 84px; top: 319px; font-size: 13.5px; color: var(--body); }
  .letter-body {
    position: absolute; left: 84px; top: 384px; width: 732px;
    font-size: 12.8px; line-height: 21.2px; color: var(--body);
    text-align: justify;
  }
  .letter-body p { margin-bottom: 21.2px; }
  .signature-mark {
    position: absolute; left: 84px; top: 871px; width: 192px; height: 42px;
    background: linear-gradient(90deg, #ececec, #dcdcdc); border-radius: 4px;
  }
  .signer { position: absolute; left: 84px; top: 944px; }
  .signer-name { font-size: 18px; font-weight: 700; color: var(--ink); }
  .signer-title { font-size: 13.5px; font-weight: 700; color: var(--body); margin-top: 4px; }
  .footer-rule { position: absolute; left: 0; top: 1125px; width: 755px; height: 2px; background: var(--ink); }
  .cert-badge {
    position: absolute; left: 722px; top: 1052px; width: 114px; height: 76px;
    background: var(--ink); border-radius: 4px;
  }
</style>
</head>
<body>
  <main class="letterhead">
    <svg class="header-swoosh" viewBox="0 0 900 220" aria-hidden="true">
      <path d="M0 0 H900 V32 C640 18 330 48 0 158 Z" fill="var(--navy)"/>
      <path d="M0 168 C300 64 600 32 880 34 C600 38 300 82 0 212 Z" fill="var(--red)"/>
    </svg>

    <div class="brand">
      <span class="brand-dot"></span>
      <span class="brand-name">KESTRO VUN</span>
    </div>

    <div class="contact">
      <div class="contact-row">
        <svg viewBox="0 0 16 16"><path d="M3 2l3 0 1 4-2 1c1 2 2 3 4 4l1-2 4 1 0 3c0 1-1 2-2 2C6 15 1 10 1 4c0-1 1-2 2-2z"/></svg>
        <span>410-555-0162</span>
      </div>
      <div class="contact-row">
        <svg viewBox="0 0 16 16"><path d="M1 3h14v10H1z M1 3l7 6 7-6" stroke="#fff" stroke-width="1"/></svg>
        <span>Info@Kestro-VUN.com</span>
      </div>
      <div class="contact-row">
        <svg viewBox="0 0 16 16"><circle cx="8" cy="8" r="7"/></svg>
        <span>www.Kestro-VUN.com</span>
      </div>
    </div>

    <div class="recipient">
      <div class="recipient-name">Dear. Mrs Mara Ellis Doyle</div>
      <div class="recipient-title">Chief Director</div>
    </div>
    <div class="letter-date">Date: 09-March-2025</div>

    <div class="letter-body">
      <p>Lorem ipsum dolor sit amet, consectetur adipiscing elit, sed do eiusmod tempor incididunt ut labore et dolore magna aliqua. Sollicitudin ac orci phasellus egestas tellus rutrum tellus. Euismod elementum nisi quis eleifend quam adipiscing vitae proin sagittis. Egestas sed tempus urna et pharetra pharetra. Quis blandit turpis cursus in hac habitasse. Sed velit dignissim sodales ut eu. Ac auctor augue mauris augue neque. In arcu cursus euismod quis viverra nibh cras pulvinar mattis. Libero justo laoreet sit amet. Felis eget nunc lobortis mattis aliquam faucibus purus in. Pulvinar etiam non quam lacus suspendisse faucibus. Odio tempor orci dapibus ultrices. Velit dignissim sodales ut eu sem integer vitae justo. Fermentum et sollicitudin ac orci phasellus egestas. Pharetra vel turpis nunc eget lorem dolor sed. Sed turpis tincidunt id aliquet risus feugiat in ante. Mus mauris vitae ultricies leo integer malesuada nunc vel. Rhoncus urna neque viverra justo nec ultrices dui. Ut placerat orci nulla pellentesque dignissim enim sit amet.</p>
      <p>Bibendum arcu vitae elementum curabitur vitae nunc. Nunc pulvinar sapien et ligula ullamcorper malesuada. At elementum eu facilisis sed. Erat pellentesque adipiscing commodo elit at imperdiet dui accumsan sit. Nunc scelerisque viverra mauris in aliquam sem fringilla. In vitae turpis massa sed. Volutpat ac tincidunt vitae semper quis lectus nulla at. Massa placerat duis ultricies lacus sed turpis. Dui vivamus arcu felis bibendum ut tristique et egestas. Blandit aliquam etiam erat velit scelerisque in dictum non consectetur. Id neque aliquam vestibulum morbi blandit cursus risus at. Sed egestas egestas fringilla phasellus faucibus scelerisque eleifend donec. Ornare quam viverra orci sagittis eu volutpat odio facilisis. Volutpat sed cras ornare arcu dui vivamus arcu. Interdum consectetur libero id faucibus nisl.</p>
      <p>Viverra mauris in aliquam sem. Mattis molestie a iaculis at erat pellentesque adipiscing commodo elit. Sit amet volutpat consequat mauris nunc. Aliquam nulla facilisi cras fermentum. Sed turpis tincidunt id aliquet risus feugiat. Augue neque gravida in fermentum et sollicitudin ac orci.</p>
    </div>

    <div class="signature-mark" role="img" aria-label="Handwritten signature of Daniel Reed Porter"></div>
    <div class="signer">
      <div class="signer-name">Daniel Reed Porter</div>
      <div class="signer-title">Chief Director</div>
    </div>

    <div class="footer-rule"></div>
    <div class="cert-badge" role="img" aria-label="QRTV certification badge"></div>
  </main>
</body>
</html>
```